Animal Adoption Page

We are working on re-designing an animal adoption page for one of our clients, and are failing to come up with a modern, cutting edge design that not only looks great, but converts well also. We would like to reach out to the brightpanel community to see some innovative design work that will help us to reach our goal. Unfortunately we can't release details of our client, so the design will need to be based on some generalisations and assumptions.
Firstly, here are some competitor pages to give you an idea of the typical animal adoption process:
- https://help.plovernet.org.uk/
- http://www.trailhounds.org.uk/microsites/sponsor-a-puppy
- http://www.halvorne.org/adopt
- http://www.globalcreaturehaven.org/adopt-an-animal
- http://www.tolbrecktrust.org/adopt
- http://www.fenstead.org.uk/adopt/default.asp
- https://give.openplains.org.uk/adopt
- http://www.qvb.org/shop/animal-adoptions/category.html
- http://www.bramleypark.org/support-us/adoptions
Secondly, here are some details that you should assume about the client:
1. Our client is heavily involved in animal conservation and have a number of animal parks/zoos in the UK
2. They have about 30 animals available for adoption, spread across 6 or 7 species (such as big cats, gorillas, elephants, etc.)
3. Each animal that you can adopt has a name, a biography, facts and personal info (date of birth, keeper, etc.)
4. There are several adoption packages to choose from:
"junior" which is aimed at children and comes with a free cuddly toy
"standard" which is aimed at everyone and has 4 different pricing levels. Each level has slightly different benefits, but usually contain an annual pass to one of the organisations animal parks/zoos. For the purposes of the design, you can choose the names of each pricing level (or if you'd prefer call them level 1, level 2, level 3 and level 4)
"virtual" is aimed at people who do not want the physical goods that come with the other adoptions packages, and just want the good feeling of helping an animal
The typical purchaser of an adoption has the following properties:
1. Most people who purchase adoptions are aged 20-45
2. Adoptions are mostly purchased BY females
3. Most adoptions are purchased FOR women
4. The majority of adoptions are purchased as gifts for other people (about 75%)
5. Gifters (people who purchase gifts for others) are the primary market we're trying to reach with the page, but other types of adopters do exist (animal lovers, people who enjoy conservation, people who want more than just a ticket to one of the parks/zoos) and these should be catered for also
What MUST the design incorporate?
- The design must show a complete design for the adoption purchase process. This includes the first page they see when they click on the "adopt" navigation link, the animal selection process, the adoption package selection process, how animal details are displayed during the process and the checkout process.
- The process must be clear and concise and very user friendly
- The design must use high quality imagery throughout. Only real photos of animals are allowed (no drawings or cartoons) but animal silhouettes are acceptable. A selection of high quality images have been provided to help guide you but you are in no way limited to using these
What SHOULD the design incorporate
- We'd like the final deign to be based on a single page website concept. You can get lots of inspiration from here - http://www.plinthgallery.com/websites/parallax/. The closest design from the current competitors is the one for halvorne.org
- The process must take into consideration conversion rates and try to be optimised
- You can design the page to use any sort of fancy javascript or jquery effects and animation. there is no need to code these, just describe how the effects will work in a document (with images where applicable)
- The design will ideally be image led, with nice large background images
What DOES NOT need to be included
- A logo design - just use a placeholder
- Any HTML or Javascript - we just need a high quality layered photoshop file from the winner
- Copy - Feel free to use lorem ipsum text where copy should go, but please describe what the copy is intended to be about either in the design or in a separate document (e.g. box 1 should contain a description of the animal species)
Colours/Brand
The new website that is being designed for the client uses two fonts throughout. For headings they use Helvetica Neue 97 Black Condensed, and for body text they use Futura PT. If you do not have these fonts, you can use equivalents but try to keep them as close to the originals as possible.
Throughout the site pages, the fonts tend to be white, and are against dark earthy coloured backgrounds. The primary palette of the site is earthy colours such as browns, greens, oranges and greys. Black is also featured heavily as a background colour.
The site comprises of lots of large background images which take up most of the users browser viewport. By default we'd like you to continue this on the adoption pages, but we're open to suggestions.
When large background images are used, and text needs to be placed over the top, the site uses semi-opaque rectangles (either 28%, 64% or 84%) as a background to the text.
Overall the site uses largely flat design principles, and when there are buttons for the user to click on, they are placed on flat rectangles (not rounded) with solid background colours.
Last comments
Overall, we are looking for something unique and cutting edge. Over the years, our client has tried using most of the approaches currently followed by our competitors with varying levels of success, but ultimately we feel there is a lot that can be done to improve the process, and are looking for a forward thinking design, that use as many cutting edge technology and design concepts as needed. We are not afraid to push the boundaries of technology and design - so feel free to think a little radically.
The winning design will be the one that provides us with the most inspiration for our final design. There are secondary prizes for any other designs that provide us with significant inspiration for our final design.
UPDATE 1: A number of designers have asked us whether the designs need to include a mobile interface. We can confirm that the smallest screensize we expect to view this page is a portrait tablet, with a screen resolution of 720px x 1024px. Anything smaller than this will be served by a separate mobile site that we will design.
UPDATE 2: From the designs we have received so far they have all had a key element missing, and we have realised this wasn't explained well enough in the original brief. We would like to see a thank you page or panel that will be displayed to the user after they have made an adoption. The elements that should be visible on this page are: 1) a thank you message, 2) the ability to share the adoption on their social networks, 3) an encouragement to share their adoption certificate on their chatterly account (probably by installing a custom chatterly app) and 4) to download a mobile app that they get free as part of their adoption
Reason: Due to requests from a few different designers we have decided to extend the deadline of this project by 5 days. This will enable all designers who have taken part to revise their designs in accordance with our feedback and provide an opportunity for new designers to submit design ideas.
- Helvetica Neue 97 black Condensed (for headers), Futura PT Body (for body)

```html
<!DOCTYPE html>
<html lang="en">
<head>
<meta charset="utf-8">
<title>Adopt an Animal – Standard Package Levels</title>
<link rel="stylesheet" href="https://fonts.googleapis.com/css2?family=Roboto:wght@100;300;400;700&display=swap">
<style>
  :root {
    --olive: #8b8566;
    --olive-dark: #6f6a4f;
    --olive-panel: rgba(140, 132, 96, 0.78);
    --grey-text: #6b6b6b;
    --white: #ffffff;
    --paper: #f6f5f1;
    --brown: #6a3a1c;
    --gold: #c98c2a;
  }
  * { box-sizing: border-box; margin: 0; padding: 0; }
  html, body { width: 1200px; height: 1059px; overflow: hidden; }
  body {
    position: relative;
    font-family: "Roboto", "Helvetica Neue", Arial, sans-serif;
    background: var(--paper);
  }

  /* Step bar */
  .step-bar {
    position: absolute; left: 0; top: 0; width: 1200px; height: 182px;
    background: linear-gradient(180deg, #ecebe6 0%, #f7f6f2 60%, #f1efe9 100%);
  }
  .hero-button {
    position: absolute; left: 418px; top: -20px; width: 364px; height: 73px;
    border: 4px solid rgba(255,255,255,0.9);
    background: rgba(225,222,212,0.6);
    color: rgba(255,255,255,0.95);
    font-weight: 700; font-size: 30px;
    display: flex; align-items: center; justify-content: center;
    padding-top: 12px;
  }
  .step {
    position: absolute; top: 72px; display: flex; align-items: center; gap: 34px;
    color: var(--olive); font-weight: 700; font-size: 33px; letter-spacing: -0.5px;
  }
  .step--package { left: 82px; }
  .step--animal { left: 468px; }
  .step__box {
    width: 32px; height: 32px; border: 3px solid var(--olive);
    background: var(--white); display: flex; align-items: center; justify-content: center;
  }
  .step__box::after { content: ""; width: 16px; height: 16px; background: var(--olive); }
  .step__label { text-decoration: line-through; text-decoration-thickness: 2px; }
  .pay-button {
    position: absolute; left: 872px; top: 58px; width: 207px; height: 66px;
    border: 3px solid var(--olive); background: var(--white);
    color: var(--olive-dark); font-weight: 700; font-size: 23px;
    display: flex; align-items: center; justify-content: center;
  }

  /* Package panel */
  .package {
    position: absolute; left: 0; top: 182px; width: 507px; height: 851px;
    background: radial-gradient(ellipse at 55% 40%, #c98a3c 0%, #9a5a22 40%, #4a2510 80%, #2a1408 100%);
  }
  .package__title {
    position: absolute; left: 0; width: 100%; top: 30px; text-align: center;
    color: var(--white); font-weight: 700; font-size: 46px; letter-spacing: -1.5px;
  }
  .package__audience {
    position: absolute; left: 0; width: 100%; top: 92px; text-align: center;
    color: var(--white); font-weight: 700; font-size: 27px; letter-spacing: -0.5px;
  }
  .package__card {
    position: absolute; left: 50px; top: 239px; width: 402px; height: 465px;
    background: rgba(255,255,255,0.93);
  }
  .package__price {
    position: absolute; left: 159px; top: 154px; width: 178px; height: 178px;
    border-radius: 50%; background: var(--white);
    border: 6px solid var(--gold);
    display: flex; align-items: center; justify-content: center;
    color: var(--grey-text); font-weight: 300; font-size: 44px;
  }
  .benefits {
    position: absolute; left: 71px; top: 148px; list-style: none;
    color: #4d4d4d; font-size: 14px; line-height: 36px;
  }
  .benefits li { position: relative; padding-left: 27px; width: 270px; }
  .benefits li::before {
    content: ""; position: absolute; left: 2px; top: 14px; width: 9px; height: 9px;
    background: #555; transform: rotate(45deg);
  }
  .level-count {
    position: absolute; left: 64px; top: 335px; width: 300px;
    color: var(--grey-text); font-size: 23px; line-height: 46px; letter-spacing: 0.3px;
  }
  .level-count__number { font-weight: 300; font-size: 60px; vertical-align: -8px; }
  .back-frame {
    position: absolute; left: 65px; top: 721px; width: 372px; height: 111px;
    border: 8px solid rgba(190,120,50,0.75);
  }
  .back-button {
    position: absolute; left: 81px; top: 737px; width: 340px; height: 79px;
    background: rgba(255,255,255,0.88);
    display: flex; align-items: center; justify-content: center; gap: 14px;
    color: var(--brown); font-weight: 700; font-size: 30px;
  }

  /* Levels */
  .levels {
    position: absolute; left: 507px; top: 182px; width: 693px; height: 851px;
    background: linear-gradient(160deg, #8f8a72 0%, #b3ad95 40%, #c9c3ad 60%, #7d7659 100%);
  }
  .level {
    position: absolute; left: 0; width: 693px;
    display: grid; grid-template-columns: 347px 346px;
  }
  .level__head, .level__text { background: var(--olive-panel); position: relative; }
  .level__head { border-right: 3px solid var(--white); }
  .level__number {
    position: absolute; left: 36px; top: 50%; transform: translateY(-50%);
    color: rgba(255,255,255,0.9); font-weight: 100; font-size: 170px; line-height: 1;
  }
  .level__name {
    position: absolute; left: 172px; top: 50%; transform: translateY(-50%);
    color: var(--white); font-weight: 300; font-size: 36px; letter-spacing: -0.5px;
  }
  .level__text p {
    position: absolute; left: 29px; top: 50%; transform: translateY(-50%); width: 265px;
    color: var(--white); font-size: 14px; line-height: 20.6px;
  }
  .level--1 { top: 0; height: 211px; }
  .level--2 { top: 211px; height: 218px; background: var(--white); padding: 12px 10px 11px 9px; }
  .level--2 .level__head, .level--2 .level__text { height: 195px; }
  .level--2 { grid-template-columns: 338px 336px; }
  .level--3 { top: 429px; height: 211px; border-bottom: 2px solid rgba(255,255,255,0.8); }
  .level--4 { top: 641px; height: 210px; }

  /* Animal strip */
  .animal-strip { position: absolute; left: 0; top: 1033px; width: 1200px; height: 26px; background: var(--white); }
  .animal-strip__photo { position: absolute; top: 0; height: 26px; }
  .animal-strip__photo--a { left: 0; width: 389px; background: linear-gradient(90deg, #e8e6e0, #d7d3c8); }
  .animal-strip__photo--b { left: 400px; width: 392px; background: linear-gradient(90deg, #c8864a, #9a6a44); }
  .animal-strip__photo--c { left: 795px; width: 405px; background: linear-gradient(90deg, #8a8a86, #4c4c4a); }
</style>
</head>
<body>

<header class="step-bar">
  <div class="hero-button">Adopt Me Today</div>
  <div class="step step--package"><span class="step__box"></span><span class="step__label">Select a package</span></div>
  <div class="step step--animal"><span class="step__box"></span><span class="step__label">Select an animal</span></div>
  <div class="pay-button">Pay now</div>
</header>

<section class="package" role="img" aria-label="Background photo of a lion's golden mane">
  <h1 class="package__title">Standard</h1>
  <p class="package__audience">For everyone</p>
  <div class="package__card">
    <ul class="benefits">
      <li>Adoption Certificate</li>
      <li>Recognition at your adopted animal's enclosure</li>
      <li>1FREE chid ticket</li>
      <li>Photo + animal fact sheet</li>
    </ul>
    <p class="level-count">We have <span class="level-count__number">4</span> levels in this package</p>
  </div>
  <div class="package__price">$69</div>
  <div class="back-frame"></div>
  <div class="back-button">
    <svg width="34" height="30" viewBox="0 0 34 30" aria-hidden="true">
      <path d="M14 2 L1 13 L14 24 L14 17 C22 17 28 20 33 28 C31 17 25 10 14 9 Z" fill="#6a3a1c"/>
    </svg>
    Back
  </div>
</section>

<section class="levels" role="img" aria-label="Background photo of fallow deer in a misty field">
  <div class="level level--1">
    <div class="level__head"><span class="level__number">1</span><span class="level__name">Level1</span></div>
    <div class="level__text"><p>Desciption of level1: Lorem ipsum dolor sit amet, consectetur adipiscing elit. Duis tincidunt odio eu magna dictum ut bibendum nulla faucibus. Aenean eget dui nulla. Sed congue adipiscing elit.</p></div>
  </div>
  <div class="level level--2">
    <div class="level__head"><span class="level__number">2</span><span class="level__name">Level2</span></div>
    <div class="level__text"><p>Desciption of level1: Lorem ipsum dolor sit amet, consectetur adipiscing elit. Duis tincidunt odio eu magna dictum ut bibendum nulla faucibus. Aenean eget dui nulla. Sed congue adipiscing elit.</p></div>
  </div>
  <div class="level level--3">
    <div class="level__head"><span class="level__number">3</span><span class="level__name">Level3</span></div>
    <div class="level__text"><p>Desciption of level1: Lorem ipsum dolor sit amet, consectetur adipiscing elit. Duis tincidunt odio eu magna dictum ut bibendum nulla faucibus. Aenean eget dui nulla. Sed congue adipiscing elit.</p></div>
  </div>
  <div class="level level--4">
    <div class="level__head"><span class="level__number">4</span><span class="level__name">Level4</span></div>
    <div class="level__text"><p>Desciption of level1: Lorem ipsum dolor sit amet, consectetur adipiscing elit. Duis tincidunt odio eu magna dictum ut bibendum nulla faucibus. Aenean eget dui nulla. Sed congue adipiscing elit.</p></div>
  </div>
</section>

<footer class="animal-strip">
  <div class="animal-strip__photo animal-strip__photo--a" role="img" aria-label="Animal photo thumbnail in pale tones"></div>
  <div class="animal-strip__photo animal-strip__photo--b" role="img" aria-label="Animal photo thumbnail in warm brown tones"></div>
  <div class="animal-strip__photo animal-strip__photo--c" role="img" aria-label="Animal photo thumbnail in grey tones"></div>
</footer>

</body>
</html>
```